Ledgerwise Reach - B2B Demand Generation Website Project

We need a fully functional website for www.ledgerwisereach.example. We are a B2B Demand Generation company, based in London, working with companies such as QRT, VKD, Norvex, Brindlow, Tarvo generating them sales leads for their sales teams. We run this through digital marketing newsletter promotions and have a network of websites. Content syndication, data, demand generation, online marketing. Our logo has just been redone (attached) and we have a holding page already which i would like to use the style / colours. Our logo is bright and vibrant but i dont want the site to be a rainbow. We are expensive, classy, professorial, B2B, intelligent.

Home
About Us
Our Services
Prospora & QA Technology
Intent Data
Testimonials
Contact Us
Updates

Target Market(s)

B2B Marketers (QRT, Velquarion, Tarvo, VKD, Opal Reach, Driftmoor, Harlow Quantis, Technology Companies, Data Companies, Marketing Teams, Tumbleden.

Industry/Entity Type

Marketing

Coding

Coded - Design and coding required

Number of Pages Required

5+ page

Font styles to use
Sans Serif

Requirements
Must have
• Home
About Us
Our Services
Prospora & QA Technology
Intent Data
Testimonials
Contact Us

Simple Pages.

Look classy, intelligent, data experts. I like the video homepages were the image moves at the top. Very soft animation.
Nice to have
• Websites i like:

https://www.vkd.example/
https://www.brevantor.example/
https://www.plumfieldsites.example.co.uk/

Ledgerwise Reach - The Demand Generation Company
Should not have
• Glimpsevault crap images

```html
<!DOCTYPE html>
<html lang="en">
<head>
<meta charset="utf-8">
<title>Ledgerwise Reach – Website Design Board</title>
<link rel="stylesheet" href="https://fonts.googleapis.com/css2?family=Poppins:wght@400;500;600;700&display=swap">
<style>
:root{
  --red:#b62522;
  --blue:#1c5d95;
  --ink:#222831;
  --muted:#6b7280;
  --board:#eaf3fc;
  --board-band:#deecfa;
  --card:#ffffff;
  --line:#e3e8ee;
  --soft:#f3f7fb;
}
*{box-sizing:border-box;margin:0;padding:0}
html,body{width:1200px;height:1200px;overflow:hidden}
body{font-family:'Poppins',sans-serif;background:var(--board);color:var(--ink);position:relative}
.abs{position:absolute}
.board-bg{position:absolute;inset:0}
.red{color:var(--red)}
.blue{color:var(--blue)}

/* brand lockup */
.brand{display:flex;align-items:center;gap:6px}
.brand-dot{border-radius:50%;background:var(--red);flex:none}
.brand-name{font-weight:500;color:var(--red);line-height:1}
.tagline{color:var(--blue);font-weight:400;white-space:nowrap}

/* page mockups */
.page{position:absolute;background:#fff;overflow:hidden}
.page-home{left:116px;top:204px;width:461px;height:839px}
.page-inner{left:623px;top:110px;width:461px;height:735px}

/* header */
.site-header{position:absolute;left:0;top:0;width:100%;height:32px;background:#fff;box-shadow:0 1px 2px rgba(0,0,0,.06);z-index:3}
.header-tab{position:absolute;left:45px;top:20px;width:72px;height:22px;background:#fff;border-radius:0 0 14px 14px;box-shadow:0 2px 3px rgba(0,0,0,.07);z-index:3}
.nav{position:absolute;top:12px;left:0;z-index:4}
.nav a{position:absolute;font-size:5.6px;color:var(--ink);text-decoration:none;white-space:nowrap}

/* hero */
.hero-glow{left:222px;top:-22px;width:252px;height:252px;border-radius:50%;background:radial-gradient(circle,rgba(182,37,34,0) 60%,rgba(182,37,34,.12) 66%,rgba(28,93,149,.07) 72%,rgba(255,255,255,0) 74%)}
.hero-photo{left:234px;top:-12px;width:236px;height:236px;border-radius:50%;background:linear-gradient(135deg,#c9d3dc 0%,#8e9aa6 45%,#4a4f58 100%)}
.eyebrow{font-size:8px}
.hero-title{font-size:14.4px;font-weight:700;color:var(--red);line-height:1.38;white-space:nowrap}
.hero-text{font-size:8px;color:#555;line-height:1.5}
.btn{position:absolute;display:flex;align-items:center;justify-content:center;gap:5px;border-radius:4px;color:#fff;font-weight:500;box-shadow:0 2px 4px rgba(0,0,0,.18)}
.btn-blue{background:var(--blue)}
.btn-red{background:var(--red)}
.btn-icon{width:9px;height:9px;border-radius:50%;background:#fff;display:flex;align-items:center;justify-content:center}

/* section heading */
.sec-head{position:absolute}
.sec-head .bubble{position:absolute;left:-9px;top:-4px;width:24px;height:24px;border:1.2px solid #dde5ee;border-right-color:transparent;border-radius:50%}
.sec-head .label{font-size:4.6px;color:var(--ink);position:relative}
.sec-head .title{font-size:11px;font-weight:700;line-height:1.15;position:relative;white-space:nowrap}

/* partners */
.partner{position:absolute;width:62px;height:30px;background:#fff;border-radius:3px;box-shadow:0 1px 4px rgba(0,0,0,.12);display:flex;align-items:center;justify-content:center;gap:3px}
.partner-mark{width:5px;height:5px;border-radius:50%;flex:none}
.partner-name{font-size:7px;font-weight:600}

/* about */
.about-glow{left:67px;top:400px;width:95px;height:95px;border-radius:50%;background:radial-gradient(circle,rgba(182,37,34,.16),rgba(182,37,34,0) 70%)}
.about-frame{left:93px;top:422px;width:131px;height:144px;background:var(--blue)}
.about-photo{left:101px;top:430px;width:129px;height:142px;background:linear-gradient(160deg,#dfe6ec,#9aa7b3 55%,#5d6671)}
.body-copy{font-size:4.4px;color:#666;line-height:1.85}

/* stats */
.burst{left:90px;top:682px;width:118px;height:118px;border-radius:50%;background:radial-gradient(circle,rgba(182,37,34,.05) 30%,rgba(182,37,34,.22) 60%,rgba(182,37,34,.08) 85%,rgba(182,37,34,0) 100%)}
.stat-small{font-size:3.6px;color:var(--red)}
.stat-num{font-size:12.4px;font-weight:600;line-height:1}
.stat-num span{color:var(--blue);font-size:9px}
.stat-label{font-size:4.8px;line-height:1.6}

/* services */
.service{position:absolute;top:59px;width:83px;height:117px;border-radius:4px;background:#fff;box-shadow:0 1px 5px rgba(0,0,0,.1);padding:14px 7px 0 7px}
.service.is-active{background:var(--blue);color:#fff}
.service h3{font-size:5.6px;font-weight:600;color:var(--blue);line-height:1.5}
.service.is-active h3{color:#fff}
.service .icon{position:absolute;left:7px;top:34px;width:38px;height:38px;border-radius:50%;background:radial-gradient(circle,#fff 35%,#fbe3e2 36%,#fdf1f1 70%);display:flex;align-items:center;justify-content:center}
.service.is-active .icon{background:radial-gradient(circle,#2a6da8 35%,#17507f 36%,#1a5890 70%)}
.service p{position:absolute;left:7px;top:84px;right:6px;font-size:4.2px;line-height:1.75;color:#666}
.service.is-active p{color:#fff}

/* QA */
.qa-photo{left:236px;top:236px;width:137px;height:161px;border-radius:8px;overflow:hidden;background:linear-gradient(135deg,#c9d2da,#6f7b86 60%,#3f4650)}
.qa-overlay{position:absolute;left:0;top:0;width:113px;height:100%;background:rgba(28,93,149,.82)}
.qa-copy{position:absolute;left:11px;color:#fff}

/* testimonials */
.avatar{position:absolute;border-radius:50%;background:linear-gradient(160deg,#c8ced6,#6c7580);border:1.5px solid #fff;box-shadow:0 1px 3px rgba(0,0,0,.15)}
.quote{font-size:4.7px;color:#555;line-height:1.75;text-align:center}

/* contact strip */
.contact-strip{left:6px;top:586px;width:455px;height:47px;background:var(--soft)}
.strip-text{font-size:4.3px;line-height:1.7}
.field{left:242px;top:601px;width:114px;height:18px;background:#fff;border:1px solid #edf0f3;font-size:3.4px;color:#aaa;padding:6px 8px}

/* footer */
.foot-title{font-size:5.4px;font-weight:600;color:var(--blue)}
.foot-item{font-size:4.4px;color:#666}
.foot-rule{left:59px;top:713px;width:351px;height:1px;background:#cfd6dd}

/* style guide */
.swatch{position:absolute;width:34px;height:34px}
.swatch-label{font-size:10px;color:var(--ink)}
</style>
</head>
<body>

<svg class="board-bg" width="1200" height="1200" aria-hidden="true">
  <polygon points="1200,125 1200,1200 95,1200" fill="var(--board-band)"/>
</svg>

<!-- board brand lockup -->
<div class="abs brand" style="left:116px;top:136px">
  <span class="brand-dot" style="width:14px;height:14px"></span>
  <span class="brand-name" style="font-size:16px">ledgerwisereach</span>
</div>
<div class="abs tagline" style="left:136px;top:159px;font-size:5.2px">The Demand Generation Company</div>

<!-- HOME PAGE -->
<section class="page page-home">
  <div class="abs hero-glow" role="img" aria-label="Soft dotted halo around the hero image"></div>
  <div class="abs hero-photo" role="img" aria-label="Photo of a team meeting around a conference table"></div>

  <header class="site-header"></header>
  <div class="header-tab"></div>
  <div class="abs brand" style="left:53px;top:24px;z-index:5;gap:3px">
    <span class="brand-dot" style="width:5px;height:5px"></span>
    <span class="brand-name" style="font-size:6px">ledgerwisereach</span>
  </div>
  <nav class="nav">
    <a style="left:185px">Home</a>
    <a style="left:212px">About Us</a>
    <a style="left:248px">Our Services</a>
    <a style="left:293px">Intent Data</a>
    <a style="left:335px">Testionials</a>
    <a style="left:376px">Contact Us</a>
  </nav>

  <div class="abs eyebrow" style="left:54px;top:81px">Welcome To</div>
  <h1 class="abs hero-title" style="left:54px;top:91px">Generate Your Demand<br>With Ledgerwise Reach</h1>
  <p class="abs hero-text" style="left:54px;top:131px;width:186px">We can assist you in delivering your demand generation strategy to your sales teams.</p>
  <div class="btn btn-blue" style="left:54px;top:166px;width:64px;height:18px;font-size:6.4px">
    <span class="btn-icon"><svg width="5" height="5" viewBox="0 0 10 10"><path d="M2 1l2 2-1 1.5c.8 1.5 1.5 2.2 3 3L7.5 6l2 2-1.5 1.5C4.5 9 1 5.5.5 1.5z" fill="var(--blue)"/></svg></span>
    contact us
  </div>

  <div class="sec-head" style="left:175px;top:236px">
    <span class="bubble"></span>
    <div class="title"><span class="red">Who we</span> <span class="blue">work with</span></div>
  </div>

  <div class="partner" style="left:54px;top:278px"><span class="partner-mark" style="background:#00a1e0"></span><span class="partner-name" style="color:#00a1e0">Cloudhaven</span></div>
  <div class="partner" style="left:126px;top:278px"><span class="partner-mark" style="background:#333"></span><span class="partner-name" style="color:#333">VKD</span></div>
  <div class="partner" style="left:198px;top:278px"><span class="partner-name" style="color:#1f70c1;font-size:9px">QRT</span></div>
  <div class="partner" style="left:270px;top:278px"><span class="partner-name" style="color:#2a6fb0">Shiftwell</span></div>
  <div class="partner" style="left:342px;top:278px"><span class="partner-mark" style="background:#0a6bb6"></span><span class="partner-name" style="color:#0a6bb6">Deltorn</span></div>

  <div class="partner" style="left:91px;top:325px"><span class="partner-name" style="color:#222">Civerra</span></div>
  <div class="partner" style="left:163px;top:325px"><span class="partner-mark" style="background:#5c4c9f"></span><span class="partner-name" style="color:#3b3b5c">Markwell</span></div>
  <div class="partner" style="left:235px;top:325px"><span class="partner-name" style="color:#049fd9">Tarvo</span></div>
  <div class="partner" style="left:307px;top:325px"><span class="partner-name" style="color:#e0312b">Orvane</span></div>

  <div class="abs about-glow" role="img" aria-label="Soft dotted decoration behind the team photo"></div>
  <div class="abs about-frame"></div>
  <div class="abs about-photo" role="img" aria-label="Photo of a presenter speaking to colleagues in an office"></div>

  <div class="sec-head" style="left:245px;top:436px">
    <span class="bubble"></span>
    <div class="label">Who we are</div>
    <div class="title"><span class="red">Know more</span> <span class="blue">about us</span></div>
  </div>
  <p class="abs body-copy" style="left:245px;top:465px;width:124px">Ledgerwise Reach can deliver high quality sales leads from any country in the world. This can include leads via email or telemarketing, account-based targeting (ABM) or identifying need and pain points through BANT / SQL campaigns.</p>
  <p class="abs body-copy" style="left:245px;top:511px;width:124px">Ledgerwise Reach offer expert demand generation support, from providing detailed leads of qualified decision-makers, to a comprehensive lead generation and SQL service.</p>
  <div class="btn btn-red" style="left:245px;top:556px;width:64px;height:17px;font-size:6.4px">know more</div>

  <div class="sec-head" style="left:178px;top:648px">
    <span class="bubble"></span>
    <div class="label">Why choose us</div>
    <div class="title"><span class="red">Discover</span> <span class="blue">your demand</span></div>
  </div>

  <div class="abs burst" role="img" aria-label="Decorative dotted circular graphic in red and blue"></div>
  <svg class="abs" style="left:0;top:0" width="461" height="839" aria-hidden="true">
    <g stroke="#f2b8b6" stroke-width=".7" fill="none">
      <polyline points="195,712 238,712 238,700 246,700"/>
      <polyline points="205,746 238,746 238,734 246,734"/>
      <polyline points="195,780 238,780 238,768 246,768"/>
    </g>
    <g stroke="#d9dee4" stroke-width=".7">
      <line x1="304" y1="695" x2="304" y2="718"/>
      <line x1="304" y1="729" x2="304" y2="752"/>
      <line x1="304" y1="764" x2="304" y2="786"/>
    </g>
  </svg>
  <div class="abs" style="left:247px;top:696px"><div class="stat-small">Ticker to</div><div class="stat-num">70,000 <span>+</span></div></div>
  <div class="abs stat-label" style="left:314px;top:699px">Download Per Month<br>Reach</div>
  <div class="abs" style="left:247px;top:730px"><div class="stat-small">Ticker to</div><div class="stat-num">25,000 <span>+</span></div></div>
  <div class="abs stat-label" style="left:314px;top:733px">Leads Delivered Per<br>Month</div>
  <div class="abs" style="left:247px;top:764px"><div class="stat-small">Ticker to</div><div class="stat-num">50 <span>+</span></div></div>
  <div class="abs stat-label" style="left:314px;top:772px">Countries We Can</div>
</section>

<!-- INNER PAGE -->
<section class="page page-inner">
  <div class="sec-head" style="left:202px;top:18px">
    <span class="bubble"></span>
    <div class="label">Our Features</div>
    <div class="title"><span class="red">Our Best</span> <span class="blue">service</span></div>
  </div>

  <article class="service" style="left:99px">
    <h3>Marketing Qualified Leads (MQL)</h3>
    <div class="icon"><svg width="11" height="10" viewBox="0 0 11 10"><rect x="1" y="5" width="2" height="5" fill="var(--red)"/><rect x="4.5" y="3" width="2" height="7" fill="var(--red)"/><rect x="8" y="1" width="2" height="9" fill="var(--red)"/></svg></div>
    <p>A Marketing Qualified Lead (MQL) is a prospect that has expressed...</p>
  </article>
  <article class="service is-active" style="left:194px">
    <h3>Account Based Marketing Leads (ABM)</h3>
    <div class="icon"><svg width="8" height="11" viewBox="0 0 8 11"><rect x=".5" y="1.5" width="7" height="9" rx="1" fill="none" stroke="#fff"/><rect x="2.5" y=".5" width="3" height="2" fill="#fff"/><line x1="2" y1="5" x2="6" y2="5" stroke="#fff"/><line x1="2" y1="7.5" x2="6" y2="7.5" stroke="#fff"/></svg></div>
    <p>ABM is a strategy that directs marketing resources to engaging a specific set...</p>
  </article>
  <article class="service" style="left:288px">
    <h3>Sales Qualified Lead or BANT</h3>
    <div class="icon"><svg width="11" height="11" viewBox="0 0 11 11"><path d="M1 5.5L5.5 1H10v4.5L5.5 10z" fill="var(--red)"/><circle cx="7.8" cy="3.2" r="1" fill="#fff"/></svg></div>
    <p>An SQL lead or a BANT lead is a type of lead that expressed a specific interest...</p>
  </article>

  <div class="sec-head" style="left:99px;top:244px">
    <span class="bubble"></span>
    <div class="label">Our Best</div>
    <div class="title"><span class="red">QA</span> <span class="blue">technology</span></div>
  </div>
  <p class="abs body-copy" style="left:99px;top:276px;width:128px">Prospora is a proprietary lead verification platform from Ledgerwise Reach that aims to sift out invalid leads with questionable or erroneous data. The platform is designed to equip sales teams with accurate, high-quality records in order to improve lead generation, accelerate pipeline and increase revenue.</p>
  <p class="abs body-copy" style="left:99px;top:328px;width:128px">Prospora is positioned to quickly identify, validate, and improve lead quality at the point-of-entry by filtering out all leads that do not match required filters, such as job title, company size, etc.</p>
  <div class="btn btn-red" style="left:99px;top:375px;width:64px;height:17px;font-size:6.4px">know more</div>

  <div class="abs qa-photo" role="img" aria-label="Photo of colleagues collaborating over documents at a desk">
    <div class="qa-overlay"></div>
    <div class="qa-copy" style="top:50px;font-size:4.8px">Expand your</div>
    <div class="qa-copy" style="top:56px;font-size:10.5px;font-weight:600;white-space:nowrap">Lead generation</div>
    <div class="qa-copy" style="top:72px;width:95px;font-size:4.2px;line-height:1.8">Our goal is to provide the most accurate lead data to ensure the best opportunity for nurture and follow up by sales and marketing teams.</div>
    <div class="qa-copy" style="top:110px;font-size:4.8px;font-weight:500">Read More....</div>
  </div>

  <div class="sec-head" style="left:206px;top:431px">
    <span class="bubble"></span>
    <div class="label">What Our Client's say</div>
    <div class="title"><span class="red">Our</span> <span class="blue">testimonials</span></div>
  </div>
  <div class="avatar" style="left:204px;top:472px;width:18px;height:18px" role="img" aria-label="Client portrait"></div>
  <div class="avatar" style="left:250px;top:472px;width:18px;height:18px" role="img" aria-label="Client portrait"></div>
  <div class="avatar" style="left:221px;top:466px;width:30px;height:30px" role="img" aria-label="Portrait of the featured client"></div>
  <svg class="abs" style="left:241px;top:486px" width="6" height="6" viewBox="0 0 6 6" aria-hidden="true"><path d="M0 6V3.5L2 0h1.2L2.2 3H3v3zM3 6V3.5L5 0h1L5 3h1v3z" fill="var(--red)"/></svg>
  <svg class="abs" style="left:104px;top:519px" width="4" height="6" aria-hidden="true"><polyline points="3,0.5 .8,3 3,5.5" fill="none" stroke="#f4c3c2" stroke-width=".8"/></svg>
  <svg class="abs" style="left:364px;top:519px" width="4" height="6" aria-hidden="true"><polyline points="1,0.5 3.2,3 1,5.5" fill="none" stroke="#f4c3c2" stroke-width=".8"/></svg>
  <p class="abs quote" style="left:125px;top:509px;width:212px">Lorem Ipsum is simply dummy text of the printing and typesetting industry. Lorem Ipsum has been the industry's standard dummy text ever since the 1500s, when an unknown printer took a galley of type and scrambled it to make a type.</p>
  <div class="abs" style="left:131px;top:541px;width:200px;text-align:center;font-size:5.4px;font-weight:600">Dorian Halvesk</div>
  <div class="abs" style="left:131px;top:549px;width:200px;text-align:center;font-size:4.2px;color:#777">Owner of xyz</div>

  <div class="abs contact-strip"></div>
  <svg class="abs" style="left:60px;top:601px" width="18" height="18" viewBox="0 0 18 18" aria-hidden="true">
    <path d="M3 6l3 3-1.5 2c1.2 2.2 2.3 3.3 4.5 4.5L11 14l3 3-2 1.5C6 17.5 1 12.5.5 6.5z" fill="none" stroke="var(--blue)" stroke-width=".8"/>
    <rect x="8" y="1" width="9" height="6" fill="none" stroke="var(--blue)" stroke-width=".8"/><polyline points="8,1 12.5,4.5 17,1" fill="none" stroke="var(--blue)" stroke-width=".8"/>
  </svg>
  <div class="abs strip-text" style="left:82px;top:603px"><b>+0 555 014 2290</b><br>hello@ledgerwise.example</div>
  <svg class="abs" style="left:144px;top:600px" width="14" height="20" viewBox="0 0 14 20" aria-hidden="true">
    <path d="M7 18S1.5 11 1.5 7a5.5 5.5 0 0111 0C12.5 11 7 18 7 18z" fill="none" stroke="var(--blue)" stroke-width=".8"/><circle cx="7" cy="7" r="2" fill="none" stroke="var(--blue)" stroke-width=".8"/><ellipse cx="7" cy="18.5" rx="5" ry="1" fill="none" stroke="var(--blue)" stroke-width=".6"/>
  </svg>
  <div class="abs strip-text" style="left:163px;top:603px">45 Quill Lane,<br>Northgate-653 453</div>
  <div class="abs field">Enter your email address here</div>
  <div class="btn btn-red" style="left:357px;top:601px;width:53px;height:18px;font-size:4.6px;border-radius:2px;box-shadow:none">Subscribe Now</div>

  <div class="abs brand" style="left:60px;top:679px;gap:3px">
    <span class="brand-dot" style="width:7px;height:7px"></span>
    <span class="brand-name" style="font-size:8.4px">ledgerwisereach</span>
  </div>
  <div class="abs tagline" style="left:71px;top:698px;font-size:3.2px">The Demand Generation Company</div>

  <div class="abs foot-title" style="left:170px;top:657px">Our Services</div>
  <div class="abs foot-item" style="left:172px;top:670px">Marketing Qualified Leads (MQL)</div>
  <div class="abs foot-item" style="left:172px;top:682px">Account Based Marketing Leads (ABM)</div>
  <div class="abs foot-item" style="left:172px;top:693px">Sales Qualified Lead or BANT</div>

  <div class="abs foot-title" style="left:273px;top:657px">Quick Links</div>
  <div class="abs foot-item" style="left:275px;top:670px">Home</div>
  <div class="abs foot-item" style="left:275px;top:682px">About Us</div>
  <div class="abs foot-item" style="left:275px;top:693px">Our Services</div>
  <div class="abs foot-item" style="left:318px;top:670px">Intent Data</div>
  <div class="abs foot-item" style="left:318px;top:682px">Testionials</div>
  <div class="abs foot-item" style="left:318px;top:693px">Contact Us</div>

  <div class="abs foot-title" style="left:362px;top:657px">Contact Us</div>
  <svg class="abs" style="left:364px;top:670px" width="8" height="30" aria-hidden="true">
    <circle cx="4" cy="3" r="3" fill="#666"/><circle cx="4" cy="14.5" r="3" fill="#666"/><circle cx="4" cy="26" r="3" fill="#666"/>
  </svg>
  <div class="abs foot-item" style="left:376px;top:670px">Chatterly</div>
  <div class="abs foot-item" style="left:376px;top:682px">Birdline</div>
  <div class="abs foot-item" style="left:376px;top:693px">Snapframe</div>

  <div class="abs foot-rule"></div>
  <div class="abs" style="left:0;top:721px;width:100%;text-align:center;font-size:3.4px;color:#888">@copyrights.ledgerwisereach. All rights reserved</div>
</section>

<!-- style guide -->
<div class="swatch" style="left:623px;top:882px;background:var(--red)"></div>
<div class="abs swatch-label" style="left:664px;top:892px">#b62522</div>
<div class="swatch" style="left:728px;top:882px;background:var(--blue)"></div>
<div class="abs swatch-label" style="left:770px;top:892px">#1c5d95</div>

<div class="abs" style="left:623px;top:933px;font-size:10px;text-decoration:underline;text-underline-offset:2px">Font-Family</div>
<div class="abs" style="left:623px;top:955px;font-size:16px;font-weight:600">Poppins <span style="font-size:9.5px;font-weight:400;margin-left:3px">60px</span></div>
<div class="abs" style="left:623px;top:979px;font-size:12px;font-weight:600">Poppins <span style="font-size:8px;font-weight:400;margin-left:3px">45px</span></div>
<div class="abs" style="left:624px;top:1000px;font-size:4.4px">Poppins <span style="margin-left:3px">18px</span></div>

</body>
</html>
```